Flyer DesignFESTIVE, FLORISTRY WORKSHOP

WE NEED A FLYER, TO SEND OUT TO PROSPECTIVE CUSTOMERS, TO ATTEND A ONE DAY CHRISTMAS WORKSHOP, ALL MATERIALS WILL BE SUPPLIED AND SO TO WE WILL PROVIDE REFRESHMENTS, PARTICIPIANTS JUST NEED TO BRING THIER FLORISTRY SCISSORS

ON THE DAY THE WILL PARTICIPIATE IN CREATING SEASONAL FLORISTRY DESIGNS THAT THEY CAN BRING HOME TO LAST THE FESTIVE SEASON,

MARGOT AND BEATRIX WILL BE THERE WITH SOME UNIQUE IDEAS TO ENHANCE OUR CHRISTMAS FESTIVITIES. TOTAL COST FOR THE DAY IS £79.00. AND THE DATE IS 6THDECEMBER, 2014, AT THE GILDEN LODGE HARWICK, WHICH HAS ALSO A BUS LINK TO MANY OTHER AREAS, SO ENJOY YOURSELVES, GET INTO THE FESTIVE FEELING ON THIS SPECIAL OCCASION

Target Market(s)

FLOWER LOVERS THAT LIKE TO CREATE THIER OWN FLORAL DESIGNS

Industry/Entity Type

Hotel

Font styles to use
Decorative

Requirements
Must have
• A CHRISTMAS ATMOSPHERE, WITH A BEAUTIFUL DOOR WREATH AND TABLE DESIGN

BOTH TUTORS ON THE DAY ARE HIGHLY SKILLED, HIGHLY QUALIFIED, WITH BEATRIX, HAVING WON NGW BRAMFORD MEDAL,
Nice to have
• BETTER WORDING THAN I HAVE GIVEN YOU

telephone number 02881430526

```html
<!DOCTYPE html>
<html lang="en">
<head>
<meta charset="utf-8">
<title>Christmas Floristry Workshop</title>
<link rel="stylesheet" href="https://fonts.googleapis.com/css2?family=Dancing+Script:wght@400;500&display=swap">
<style>
  :root {
    --ink: #1b1816;
    --paper: #ffffff;
    --mist-rose: #f3eaec;
    --mist-leaf: #edf1ea;
    --garland-red: #e2a3a6;
    --garland-green: #dfe8dc;
    --wreath-purple: #b0709f;
    --wreath-green: #8fa886;
  }
  * { margin: 0; padding: 0; box-sizing: border-box; }
  html, body { width: 851px; height: 1200px; overflow: hidden; background: var(--paper); }
  .flyer {
    position: relative;
    width: 851px;
    height: 1200px;
    overflow: hidden;
    font-family: "Dancing Script", cursive;
    color: var(--ink);
    background: var(--paper);
  }
  .flyer__backdrop {
    position: absolute;
    left: 0; top: 127px;
    width: 851px; height: 1073px;
    background: linear-gradient(160deg, var(--mist-rose) 0%, var(--paper) 45%, var(--mist-leaf) 100%);
  }
  .flyer__garland {
    position: absolute;
    left: 0; top: 0;
    width: 851px; height: 127px;
    background: linear-gradient(180deg, var(--garland-red) 0%, var(--garland-green) 100%);
  }
  .flyer__title {
    position: absolute;
    top: 143px; left: 0; width: 100%;
    text-align: center;
    font-weight: 400;
    font-size: 47px;
    line-height: 60px;
    letter-spacing: 1px;
  }
  .flyer__wreath {
    position: absolute;
    left: 251px; top: 237px;
    width: 352px; height: 357px;
    background: linear-gradient(135deg, var(--wreath-purple) 0%, var(--wreath-green) 100%);
  }
  .event {
    position: absolute;
    left: 0; width: 100%;
    text-align: center;
  }
  .event__date { top: 594px; font-size: 46px; line-height: 56px; font-weight: 500; }
  .event__venue { top: 643px; font-size: 39px; line-height: 48px; font-weight: 500; }
  .event__address { top: 703px; font-size: 20px; line-height: 26px; }
  .copy {
    position: absolute;
    left: 0; width: 100%;
    text-align: center;
    font-size: 25px;
    line-height: 34px;
  }
  .copy--intro { top: 757px; }
  .copy--tutors { top: 866px; }
  .copy--refresh { top: 976px; }
  .copy--bring { top: 1046px; }
  .copy--price { top: 1116px; font-size: 28px; line-height: 36px; }
  .copy--contact { top: 1150px; font-size: 28px; line-height: 36px; }
</style>
</head>
<body>
<main class="flyer">
  <div class="flyer__backdrop" role="img" aria-label="Faint photograph of a florist trimming white flowers with scissors"></div>
  <div class="flyer__garland" role="img" aria-label="Christmas garland with red bow, baubles and bells"></div>

  <h1 class="flyer__title">CHRISTMAS FLORISTRY WORKSHOP</h1>

  <div class="flyer__wreath" role="img" aria-label="Round door wreath of purple, yellow and red flowers with green foliage"></div>

  <p class="event event__date">6th Dec, 2014</p>
  <p class="event event__venue">The Gilden Lodge</p>
  <p class="event event__address">18-24 Mill Brook Rd, Harwick</p>

  <p class="copy copy--intro">Celebrate this Christmas by attending a seasonal floristry workshop<br>run by highly skilled and qualified instructors.</p>
  <p class="copy copy--tutors">Workshop will be conducted by Margot and Beatrix, a NGW Bramford<br>Medal winner.</p>
  <p class="copy copy--refresh">Refreshments will be provided!</p>
  <p class="copy copy--bring">Just bring your creative ideas and floristry sissors, we will provide<br>all the required material and supplies.</p>
  <p class="copy copy--price">Cost £79.00</p>
  <p class="copy copy--contact">Contact: 02881430526</p>
</main>
</body>
</html>
```